App Design for Diary & Todo Do List Android App

This project is to create a four screen design for Velmo Ledger which is a Diary, Journal, Notepad and Todo List App. All information about this design can be found in https://lnk.example-short.net/Qw7TzB
I have also attached same as PDF

Velmo Ledger is private Diary, Journal, Notes & Todo List app for professionals and home users. This is to design 4 screens for Velmo Ledger Android App and they are:

1. Note List Screen
2. Todo List Screen
3. Task List Screen
4. Add Task Screen

The main goal of this design are

Good user experience
Good app design

Diary app, Notepad app, and Todo List are common app category so the goal of this design is to create a simple, intuitive and elegant design. I have included my own attempt as example in this Google Doc https://lnk.example-short.net/Qw7TzB

Target Market(s)

Brightshelf App Market

Industry/Entity Type

Android

Font styles to use
Serif
Sans Serif
Script

Colors

Designer to choose colors to be used in the design.

Requirements
Must have
• Elegant and intuitive design that makes it easy for people to add and complete Todo List tasks and enter journal.
Nice to have
• New app icon
Should not have
• N/A

```html
<!DOCTYPE html>
<html lang="en">
<head>
<meta charset="utf-8">
<title>Velmo Ledger – Add New List</title>
<link rel="stylesheet" href="https://fonts.googleapis.com/css2?family=Nunito+Sans:wght@300;400;600&display=swap">
<style>
  :root {
    --page-bg: #eef0f2;
    --screen-bg: #ffffff;
    --green-dark: #4fab00;
    --green-light: #7bd600;
    --green-accent: #52b012;
    --green-soft: #9fd67a;
    --icon-green: #8fd33f;
    --text-main: #2b2b2b;
    --text-label: #8a8a8a;
    --divider: #e2e2e2;
    --tab-bg: #ffffff;
  }
  * { box-sizing: border-box; margin: 0; padding: 0; }
  html, body {
    width: 1000px; height: 1200px; overflow: hidden;
    background: var(--page-bg);
    font-family: "Nunito Sans", "Avenir Next", sans-serif;
    color: var(--text-main);
  }
  .screen {
    position: absolute; left: 162px; top: 0;
    width: 676px; height: 1200px;
    background: var(--screen-bg);
    overflow: hidden;
  }
  .app-header {
    position: absolute; left: 0; top: 0; width: 100%; height: 134px;
    background: linear-gradient(100deg, var(--green-dark) 0%, var(--green-light) 100%);
    color: #fff;
  }
  .status-bar {
    position: absolute; left: 0; top: 6px; width: 100%; height: 26px;
    font-size: 19px; font-weight: 600;
  }
  .status-bar .signal { position: absolute; left: 16px; top: 4px; }
  .status-bar .clock { position: absolute; left: 0; width: 100%; text-align: center; top: 0; line-height: 26px; }
  .status-bar .battery { position: absolute; right: 10px; top: 0; line-height: 26px; display: flex; align-items: center; gap: 8px; }
  .header-title {
    position: absolute; left: 0; width: 100%; top: 58px;
    text-align: center; font-size: 32px; font-weight: 400; line-height: 42px;
  }
  .header-confirm { position: absolute; right: 32px; top: 62px; }

  .field-label, .field-value, .add-tasks { position: absolute; white-space: nowrap; }
  .field-label {
    font-size: 17px; letter-spacing: 1.6px; color: var(--text-label);
    text-transform: uppercase; line-height: 22px; font-weight: 400;
  }
  .field-value { font-size: 23px; line-height: 30px; font-weight: 400; }
  .divider { position: absolute; height: 2px; background: var(--divider); }
  .chevron { position: absolute; }

  .toggle { position: absolute; left: 560px; top: 211px; width: 70px; height: 36px; }
  .toggle .track { position: absolute; left: 0; top: 6px; width: 60px; height: 24px; border-radius: 12px; background: var(--green-soft); }
  .toggle .knob { position: absolute; left: 34px; top: 0; width: 36px; height: 36px; border-radius: 50%; background: var(--green-accent); }

  .add-tasks {
    left: 53px; top: 1022px; display: flex; align-items: center; gap: 14px;
    color: var(--green-accent); font-size: 25px; line-height: 30px;
  }

  .tab-bar {
    position: absolute; left: 0; bottom: 0; width: 100%; height: 102px;
    background: var(--tab-bg);
    box-shadow: 0 -14px 24px rgba(0,0,0,0.05);
    display: flex; justify-content: space-around; align-items: center;
    padding: 0 28px;
  }
</style>
</head>
<body>
<main class="screen">
  <header class="app-header">
    <div class="status-bar">
      <svg class="signal" width="80" height="16" viewBox="0 0 80 16">
        <circle cx="6" cy="8" r="5" fill="#fff"/><circle cx="18" cy="8" r="5" fill="#fff"/><circle cx="30" cy="8" r="5" fill="#fff"/>
        <circle cx="42" cy="8" r="4.3" fill="none" stroke="#fff" stroke-width="1.3"/><circle cx="54" cy="8" r="4.3" fill="none" stroke="#fff" stroke-width="1.3"/>
        <path d="M70 14 l-3-3 a4.5 4.5 0 0 1 6 0z M64 8 a9 9 0 0 1 12 0 M61.5 5 a13 13 0 0 1 17 0" fill="#fff" stroke="#fff" stroke-width="1.8" stroke-linecap="round"/>
      </svg>
      <div class="clock">12:00</div>
      <div class="battery">
        <span>100%</span>
        <svg width="44" height="18" viewBox="0 0 44 18"><rect x="1" y="1" width="38" height="16" rx="3" fill="none" stroke="#fff" stroke-width="1.5"/><rect x="3" y="3" width="34" height="12" rx="1.5" fill="#fff"/><rect x="40" y="6" width="3" height="6" rx="1" fill="#fff"/></svg>
      </div>
    </div>
    <h1 class="header-title">Add New List</h1>
    <svg class="header-confirm" width="40" height="32" viewBox="0 0 40 32"><path d="M3 16 L14 27 L37 4" fill="none" stroke="#fff" stroke-width="4" stroke-linecap="round" stroke-linejoin="round"/></svg>
  </header>

  <section class="form">
    <div class="field-label" style="left:53px;top:172px">Set for urgent</div>
    <div class="field-value" style="left:53px;top:214px">Urgent</div>
    <div class="toggle"><span class="track"></span><span class="knob"></span></div>
    <div class="divider" style="left:53px;top:282px;width:570px"></div>

    <div class="field-label" style="left:53px;top:326px">Title</div>
    <div class="field-value" style="left:53px;top:368px">Meeting with Odile</div>
    <div class="divider" style="left:53px;top:437px;width:570px"></div>

    <div class="field-label" style="left:53px;top:484px">Date</div>
    <div class="field-value" style="left:53px;top:526px">March 9, 2015</div>
    <div class="divider" style="left:53px;top:577px;width:570px"></div>

    <div class="field-label" style="left:53px;top:614px">From</div>
    <div class="field-value" style="left:53px;top:657px">8:00am</div>
    <div class="divider" style="left:53px;top:707px;width:264px"></div>
    <div class="field-label" style="left:365px;top:614px">To</div>
    <div class="field-value" style="left:365px;top:657px">10:00am</div>
    <div class="divider" style="left:364px;top:707px;width:266px"></div>

    <div class="field-label" style="left:53px;top:746px">Notify</div>
    <div class="field-value" style="left:53px;top:789px">every 20 minutes</div>
    <svg class="chevron" style="left:586px;top:797px" width="22" height="14" viewBox="0 0 22 14"><path d="M1 2 L11 12 L21 2" fill="none" stroke="#8a8a8a" stroke-width="1.8"/></svg>
    <div class="divider" style="left:53px;top:839px;width:570px"></div>

    <div class="field-label" style="left:53px;top:876px">Add to list</div>
    <div class="field-value" style="left:53px;top:920px">Personal</div>
    <svg class="chevron" style="left:586px;top:928px" width="22" height="14" viewBox="0 0 22 14"><path d="M1 2 L11 12 L21 2" fill="none" stroke="#8a8a8a" stroke-width="1.8"/></svg>
    <div class="divider" style="left:53px;top:969px;width:570px"></div>

    <div class="add-tasks">
      <svg width="28" height="26" viewBox="0 0 28 26" fill="var(--green-accent)">
        <circle cx="3" cy="3" r="2.2"/><circle cx="3" cy="10" r="2.2"/><circle cx="3" cy="17" r="2.2"/><circle cx="3" cy="24" r="2.2"/>
        <rect x="9" y="2" width="18" height="2"/><rect x="12" y="9" width="15" height="2"/><rect x="12" y="16" width="15" height="2"/><rect x="9" y="23" width="18" height="2"/>
      </svg>
      <span>Add Tasks</span>
    </div>
  </section>

  <nav class="tab-bar">
    <svg width="52" height="46" viewBox="0 0 52 46" aria-label="Notes">
      <rect x="10" y="2" width="38" height="40" fill="none" stroke="var(--icon-green)" stroke-width="3"/>
      <rect x="2" y="8" width="40" height="36" fill="var(--icon-green)"/>
      <rect x="8" y="16" width="14" height="10" fill="#fff"/><rect x="8" y="30" width="28" height="3" fill="#fff"/><rect x="8" y="36" width="28" height="3" fill="#fff"/>
    </svg>
    <svg width="50" height="44" viewBox="0 0 50 44" aria-label="Todo lists">
      <path d="M1 5 l4 4 l7 -8" fill="none" stroke="var(--green-accent)" stroke-width="3"/>
      <circle cx="5" cy="22" r="3.2" fill="var(--green-accent)"/><circle cx="5" cy="38" r="3.2" fill="var(--green-accent)"/>
      <rect x="16" y="3" width="32" height="3" fill="var(--green-accent)"/><rect x="20" y="12" width="28" height="3" fill="var(--green-accent)"/>
      <rect x="16" y="20" width="32" height="3" fill="var(--green-accent)"/><rect x="20" y="28" width="28" height="3" fill="var(--green-accent)"/>
      <rect x="16" y="36" width="32" height="3" fill="var(--green-accent)"/>
    </svg>
    <svg width="52" height="44" viewBox="0 0 52 44" aria-label="Folders">
      <path d="M2 6 h16 l4 4 h26 v30 h-46z" fill="var(--icon-green)" opacity="0.75"/>
      <path d="M6 16 h44 l-6 26 h-42z" fill="var(--icon-green)"/>
    </svg>
    <svg width="48" height="46" viewBox="0 0 48 46" aria-label="Settings" fill="none" stroke="var(--icon-green)" stroke-width="3.5">
      <circle cx="14" cy="24" r="9" stroke-dasharray="5 2.5"/><circle cx="14" cy="24" r="3.5" stroke-width="2.5"/>
      <circle cx="36" cy="10" r="7" stroke-dasharray="4 2"/><circle cx="36" cy="36" r="7" stroke-dasharray="4 2"/>
    </svg>
  </nav>
</main>
</body>
</html>
```